banner ad

We're looking for a banner similar to the one shown on the attached file. The same 4 keywords, the same text up top, but with new formatting, design and perhaps color scheme. Looking for something to catch people's attention that will stand out on this particular page shown in the attached image. Our goal is to find a banner with a better click through rate than the current version.

```html
<!DOCTYPE html>
<html lang="en">
<head>
<meta charset="utf-8">
<title>Blood Glucose Banner</title>
<link href="https://fonts.googleapis.com/css2?family=Arimo:wght@400;700&display=swap" rel="stylesheet">
<style>
  :root {
    --navy: #0b2545;
    --navy-light: #14396b;
    --sky: #00b4d8;
    --ocean: #0077b6;
    --amber: #ffd166;
    --white: #ffffff;
    --mist: rgba(255, 255, 255, 0.08);
  }
  * { margin: 0; padding: 0; box-sizing: border-box; }
  html, body { width: 1200px; height: 195px; overflow: hidden; background: var(--navy); }
  .banner {
    position: relative;
    width: 1200px;
    height: 195px;
    overflow: hidden;
    font-family: "Arimo", Arial, sans-serif;
    background: linear-gradient(120deg, var(--navy) 0%, var(--navy-light) 100%);
  }
  .backdrop { position: absolute; inset: 0; }
  .header {
    position: absolute;
    left: 24px; right: 24px; top: 0;
    height: 44px;
    display: flex;
    align-items: center;
    justify-content: space-between;
  }
  .heading {
    display: flex;
    align-items: center;
    gap: 10px;
    color: var(--white);
    font-size: 21px;
    font-weight: 700;
  }
  .heading-mark {
    width: 12px; height: 12px;
    border-radius: 50%;
    background: var(--amber);
  }
  .ad-label {
    color: rgba(255, 255, 255, 0.6);
    font-size: 12px;
    letter-spacing: 1.5px;
  }
  .keywords {
    position: absolute;
    left: 24px; top: 50px;
    width: 1152px;
    display: grid;
    grid-template-columns: 1fr 1fr;
    grid-auto-rows: 60px;
    gap: 12px 16px;
  }
  .keyword {
    display: flex;
    align-items: center;
    justify-content: space-between;
    padding: 0 10px 0 28px;
    border-radius: 30px;
    background: linear-gradient(90deg, var(--sky) 0%, var(--ocean) 100%);
    box-shadow: 0 4px 10px rgba(0, 0, 0, 0.3);
    color: var(--white);
    font-size: 29px;
    font-weight: 700;
    text-decoration: none;
    white-space: nowrap;
  }
  .keyword-arrow {
    flex: none;
    width: 42px; height: 42px;
    border-radius: 50%;
    background: var(--amber);
    display: flex;
    align-items: center;
    justify-content: center;
  }
</style>
</head>
<body>
<div class="banner">
  <svg class="backdrop" width="1200" height="195" aria-hidden="true">
    <circle cx="1120" cy="-20" r="140" fill="var(--mist)"/>
    <circle cx="40" cy="230" r="110" fill="var(--mist)"/>
  </svg>

  <div class="header">
    <div class="heading"><span class="heading-mark"></span>Ads Related to blood glucose</div>
    <div class="ad-label">ADVERTISEMENT</div>
  </div>

  <div class="keywords">
    <a class="keyword" href="#">Blood Glucose
      <span class="keyword-arrow"><svg width="18" height="18" viewBox="0 0 18 18" aria-hidden="true"><path d="M6 3 L12 9 L6 15" fill="none" stroke="#0b2545" stroke-width="3" stroke-linecap="round" stroke-linejoin="round"/></svg></span>
    </a>
    <a class="keyword" href="#">Blood Sugar Levels Chart
      <span class="keyword-arrow"><svg width="18" height="18" viewBox="0 0 18 18" aria-hidden="true"><path d="M6 3 L12 9 L6 15" fill="none" stroke="#0b2545" stroke-width="3" stroke-linecap="round" stroke-linejoin="round"/></svg></span>
    </a>
    <a class="keyword" href="#">Normal Blood Sugar Range
      <span class="keyword-arrow"><svg width="18" height="18" viewBox="0 0 18 18" aria-hidden="true"><path d="M6 3 L12 9 L6 15" fill="none" stroke="#0b2545" stroke-width="3" stroke-linecap="round" stroke-linejoin="round"/></svg></span>
    </a>
    <a class="keyword" href="#">What Is Normal Blood Sugar
      <span class="keyword-arrow"><svg width="18" height="18" viewBox="0 0 18 18" aria-hidden="true"><path d="M6 3 L12 9 L6 15" fill="none" stroke="#0b2545" stroke-width="3" stroke-linecap="round" stroke-linejoin="round"/></svg></span>
    </a>
  </div>
</div>
</body>
</html>
```